Flier needed for parenting seminar

Hello! We need a 4 by 6 clubcard needed for an upcoming parenting seminar. Flier should be in color, good quality images, and be front/back.
We are looking for something fresh, eye-catching, and not generic. Thanks!
CLUBCARD FRONT:
Veltran Institute presents:
Hearthbound Parenting:
Growing Steadfast Homes
By Shaykh Idris Kamal Tarbusi
Sat & Sun
Oct 22 & 23, 2016
9am - 7pm
Location: ORB Samira Hall
4187 Marlow Blvd
Santa Clara, CA 95127
Seating is limited. Register now!
Www.VeltranInstitute.com
1-877-Veltra7
CLUBCARD BACK:
There are no guarantees in life as to raising children to be how they should. Indeed, even Noah (as) lost his son while the Pharaoh's wife was able to raise Moses (as). And while traditionally a woman rears the child, Zakariyah (as) was a man chosen to raise one. The variety of scenarios in the Quran cover all possibilities. It is therefore worth reflecting on them to gain insight and draw parenting lessons.
So come and explore the Quranic view and prophetic guidelines for raising children. We hope this course serves as a landmark for you to know best practices and tools available to you, rooted in Quranic wisdom as well as our own experiences.
Some topics:
- The ways of Quranic raising
- Tools & examples from The Book
- What not to do
- Truth vs wisdom
www.VeltranInstitute.com
1-877-Veltra7
Parents, ppl considering becoming parents, ppl studying child development
- Fresh
- Eye-catching, not generic.
- Silhouette of mother/father with a young child.
- Maybe even praying together...

```html
<!DOCTYPE html>
<html lang="en">
<head>
<meta charset="utf-8">
<title>Hearthbound Parenting Clubcard</title>
<link href="https://fonts.googleapis.com/css2?family=Marcellus&family=Tenor+Sans&display=swap" rel="stylesheet">
<style>
  :root {
    --page: #ffffff;
    --olive: #a3a23c;
    --olive-light: #c9c66a;
    --panel: rgba(253, 238, 170, 0.86);
    --ink: #1d1a14;
    --night: #121210;
    --cream: #ece6c8;
    --sun-top: #f6c75a;
    --sun-mid: #f3a92e;
    --sun-low: #d9821c;
    --ground: #2a1a0c;
  }
  * { box-sizing: border-box; margin: 0; padding: 0; }
  html, body { width: 890px; height: 1200px; overflow: hidden; background: var(--page); }
  body { position: relative; font-family: "Marcellus", serif; color: var(--ink); }

  .card { position: absolute; left: 29px; width: 801px; height: 541px; overflow: hidden;
          box-shadow: 6px 10px 18px rgba(0,0,0,0.35); }
  .card--front { top: 31px; }
  .card--back { top: 598px; background: var(--night); }

  .sunset-photo { position: absolute; inset: 0;
    background:
      linear-gradient(to bottom, transparent 78%, var(--ground) 100%),
      radial-gradient(ellipse at 30% 80%, #fff3b0 0%, transparent 45%),
      linear-gradient(to bottom, var(--sun-top) 0%, var(--sun-mid) 55%, var(--sun-low) 100%); }

  .info-panel { position: absolute; left: 22px; top: 46px; width: 338px; height: 426px;
    background: var(--panel); border: 3px solid var(--olive); outline: 1px solid var(--olive);
    outline-offset: -8px; text-align: center; }
  .info-panel > * { position: absolute; left: 0; right: 0; white-space: nowrap; line-height: 1.2; }
  .presenter { top: 26px; font-family: "Tenor Sans", sans-serif; font-style: italic; font-size: 15px; }
  .title { top: 50px; font-size: 22px; font-weight: 400; letter-spacing: -0.3px; }
  .title span { display: block; font-size: 24px; margin-top: 4px; letter-spacing: 0; }
  .speaker { top: 120px; font-size: 17px; }
  .divider { top: 159px; left: 114px; right: auto; }
  .when { top: 178px; font-size: 20px; line-height: 26px; white-space: normal; }
  .where { top: 267px; font-size: 19px; }
  .address { top: 292px; font-size: 14px; }
  .cta { top: 328px; font-size: 14px; text-decoration: underline; }
  .web { top: 348px; font-size: 16px; font-variant: small-caps; letter-spacing: 0.5px; }
  .phone { top: 372px; font-size: 23px; }

  .frame { position: absolute; inset: 22px; border: 3px solid var(--olive);
    outline: 1px solid var(--olive); outline-offset: -8px; }
  .back-copy { position: absolute; left: 55px; top: 52px; width: 690px; color: var(--cream); }
  .back-title { font-size: 19px; font-weight: 400; line-height: 22px; color: var(--olive-light); }
  .back-title span { display: block; font-size: 17px; }
  .back-copy p, .topics { font-family: "Tenor Sans", sans-serif; font-size: 14.8px; line-height: 21px; margin-top: 13px; }
  .topics { list-style: none; margin-top: 18px; }
  .back-cta { position: absolute; left: 55px; width: 380px; text-align: center; color: var(--olive-light); white-space: nowrap; }
  .back-cta--call { top: 426px; font-size: 17px; line-height: 22px; }
  .back-cta--web { top: 456px; font-size: 16px; line-height: 22px; }
  .family-art { position: absolute; left: 483px; top: 292px; width: 245px; height: 207px;
    border-radius: 40px 40px 20px 20px;
    background: linear-gradient(120deg, #1c4fb0 0%, #3da8e0 55%, #5cc23a 100%); }
</style>
</head>
<body>
  <section class="card card--front">
    <div class="sunset-photo" role="img" aria-label="Photo of a family silhouetted against a golden sunset, parents joining hands above two children"></div>
    <div class="info-panel">
      <p class="presenter">Veltran Institute presents:</p>
      <h1 class="title">HEARTHBOUND PARENTING:<span>Growing Steadfast Homes</span></h1>
      <p class="speaker">by Shaykh Idris Kamal Tarbusi</p>
      <svg class="divider" width="110" height="8" viewBox="0 0 110 8" aria-hidden="true">
        <line x1="0" y1="4" x2="110" y2="4" stroke="#1d1a14" stroke-width="1"/>
        <circle cx="55" cy="4" r="2.5" fill="#1d1a14"/>
      </svg>
      <p class="when">Saturday &amp; Sunday<br>Oct. 22 &amp; 23, 2016<br>9am - 7pm</p>
      <p class="where">Location: ORB Samira Hall</p>
      <p class="address">4187 Marlow Blvd, Santa Clara, CA 95127</p>
      <p class="cta">SEATING IS LIMITED. REGISTER NOW!</p>
      <p class="web">www.VeltranInstitute.com</p>
      <p class="phone">1-877-VELTRA7</p>
    </div>
  </section>

  <section class="card card--back">
    <div class="frame"></div>
    <div class="back-copy">
      <h2 class="back-title">HEARTHBOUND PARENTING: Growing Steadfast Homes<span>by Shaykh Idris Kamal Tarbusi</span></h2>
      <p>There are no guarantees in life as to raising children to be how they should. Indeed, even Noah (as) lost his son while the Pharaoh's wife was able to raise Moses (as). And while traditionally a woman rears the child, Zakariyah (as) was a man chosen to raise one. The variety of scenarios in the Quran cover all possibilities. It is therefore worth reflecting on them to gain insight and draw parenting lessons.</p>
      <p>So come and explore the Quranic view and prophetic guidelines for raising children. We hope this course serves as a landmark for you to know best practices and tools available to you, rooted in Quranic wisdom as well as our own experiences.</p>
      <ul class="topics">
        <li>Some topics:</li>
        <li>- The ways of Quranic raising</li>
        <li>- Tools &amp; examples from The Book</li>
        <li>- What not to do</li>
        <li>- Truth vs wisdom</li>
      </ul>
    </div>
    <p class="back-cta back-cta--call">SEATING IS LIMITED. REGISTER NOW!</p>
    <p class="back-cta back-cta--web">www.VeltranInstitute.com<br>1-877-VELTRA7</p>
    <div class="family-art" role="img" aria-label="Illustration of a mother and two children seated together reading a book"></div>
  </section>
</body>
</html>
```